We need a web page design for a new company called "Brindle". We provide an innovative music sharing mobile application that allows music listeners to share their music without paying for a monthly subscription. We would like to incorporate the attached logo and color scheme. The final design should communicate music gifting and sharing.

Industry/Entity Type

It Company

```html
<!DOCTYPE html>
<html lang="en">
<head>
<meta charset="utf-8">
<title>Brindle – share your music</title>
<link href="https://fonts.googleapis.com/css2?family=Exo+2:wght@300;400;500&family=Open+Sans:wght@400;600;700&display=swap" rel="stylesheet">
<style>
:root{
  --green:#6ea25a;
  --green-dark:#5d8f4b;
  --ink:#3c3c3c;
  --grey-text:#7a7a7a;
  --pale-band:#dfe7df;
  --white:#ffffff;
  --footer:#3b3b3b;
  --panel:rgba(70,70,70,.78);
}
*{box-sizing:border-box;margin:0;padding:0}
html,body{width:796px;height:1200px;overflow:hidden}
body{position:relative;background:var(--white);font-family:"Open Sans",Arial,sans-serif;color:var(--ink)}
.heading{font-family:"Exo 2",Arial,sans-serif}

/* header */
.site-header{position:absolute;left:0;top:0;width:796px;height:92px;background:var(--green)}
.brand{position:absolute;left:68px;top:22px;display:flex;align-items:center;gap:10px;color:var(--white)}
.brand-dot{width:36px;height:36px;border-radius:50%;background:var(--white)}
.brand-name{font-family:"Exo 2",Arial,sans-serif;font-size:38px;font-weight:500;line-height:1}
.main-nav{position:absolute;top:41px;left:0;width:796px;font-size:10.5px;color:var(--white);text-transform:uppercase}
.main-nav a{position:absolute;color:inherit;text-decoration:none;white-space:nowrap}

/* hero */
.hero{position:absolute;left:0;top:92px;width:796px;height:391px;background:linear-gradient(120deg,#e9e9e7 0%,#d8d8d5 55%,#cfcfcc 100%);overflow:hidden}
.hero-device{position:absolute;left:95px;top:126px;width:260px;height:265px;border-radius:34px 34px 0 0;background:linear-gradient(180deg,#2d2d2d,#111)}
.hero-device .screen{position:absolute;left:18px;top:82px;width:214px;height:183px;background:var(--green)}
.download-title{position:absolute;left:502px;top:104px;width:229px;height:49px;background:var(--green);color:var(--white);font-size:21px;font-weight:300;line-height:1;white-space:nowrap;display:flex;align-items:center;justify-content:center;letter-spacing:0}
.download-panel{position:absolute;left:463px;top:155px;width:268px;height:146px;background:var(--panel);color:var(--white)}
.download-panel .tagline{position:absolute;right:14px;top:14px;font-size:19px;font-weight:300;white-space:nowrap}
.download-panel p{position:absolute;left:12px;top:48px;width:246px;font-size:8.2px;line-height:13px;color:#e4e4e4}
.btn-more{position:absolute;left:3px;top:116px;width:86px;height:27px;background:var(--green);color:var(--white);font-size:8.5px;display:flex;align-items:center;justify-content:center;white-space:nowrap}
.slider-dots{position:absolute;left:692px;top:369px;display:flex;gap:2px}
.slider-dots span{width:9px;height:9px;background:var(--green)}
.slider-dots span.is-active{background:#4a4a4a}

/* tweet */
.tweet{position:absolute;left:0;top:483px;width:796px;height:155px;background:var(--white)}
.tweet-mark{position:absolute;left:101px;top:42px;width:58px;height:58px;border-radius:50%;background:#6f6f6f}
.tweet-text{position:absolute;left:179px;top:36px;width:560px;font-size:24px;font-weight:300;line-height:32px;color:#777}
.tweet-text .link{color:var(--green);font-weight:400}
.tweet-meta{position:absolute;left:179px;top:103px;font-size:10.5px;color:#9a9a9a}

/* news + welcome */
.content-band{position:absolute;left:0;top:638px;width:796px;height:304px;background:var(--pale-band)}
.section-title{position:absolute;font-size:16px;font-weight:400;color:#555;white-space:nowrap}
.news-card{position:absolute;left:66px;width:270px;height:71px;background:var(--white)}
.news-card .thumb{position:absolute;left:0;top:0;width:85px;height:71px}
.news-card p{position:absolute;left:97px;top:9px;width:165px;font-size:7.2px;line-height:10.5px;color:#555}
.news-card .more{position:absolute;left:97px;bottom:6px;font-size:7px;color:var(--green)}
.news-card .date{position:absolute;right:10px;bottom:6px;font-size:7px;color:var(--green)}
.welcome-box{position:absolute;left:360px;top:44px;width:372px;height:243px;background:var(--white);padding:18px 20px 0 20px;font-size:8.4px;line-height:14.5px;color:#555;overflow:hidden}
.welcome-photo{float:right;width:142px;height:117px;margin:8px 2px 6px 14px;background:linear-gradient(135deg,#3a2e2a,#1a1616 60%,#5a4438)}
.drop-cap{float:left;font-family:"Exo 2",Arial,sans-serif;font-size:24px;line-height:22px;margin:2px 2px 0 0;color:#444}

/* clients */
.clients{position:absolute;left:0;top:942px;width:796px;height:175px;background:var(--white)}
.clients .section-title{left:0;width:796px;top:24px;text-align:center}
.client-row{position:absolute;left:0;width:796px;display:flex;justify-content:center;gap:17px;font-size:12px;font-weight:600;color:#6a6a6a;white-space:nowrap}
.client-row span{display:flex;align-items:center;gap:4px}
.client-row i{display:inline-block;width:8px;height:8px;border-radius:50%;background:#6a6a6a}

/* footer */
.site-footer{position:absolute;left:0;top:1117px;width:796px;height:83px;background:var(--footer);color:#bdbdbd}
.footer-brand{position:absolute;left:68px;top:18px;display:flex;align-items:center;gap:8px;color:#8a8a8a}
.footer-brand .brand-dot{width:24px;height:24px;background:#8a8a8a}
.footer-brand .brand-name{font-size:24px}
.copyright{position:absolute;left:68px;top:57px;font-size:7.5px}
.social-links{position:absolute;left:597px;top:20px;display:flex;gap:4px}
.social-links span{width:16px;height:16px;border-radius:2px}
.footer-nav{position:absolute;right:70px;top:56px;font-size:7.5px;display:flex}
.footer-nav a{color:#d0d0d0;text-decoration:none;padding:0 9px;border-left:1px solid #777}
.footer-nav a:first-child{border-left:none}
</style>
</head>
<body>

<header class="site-header">
  <div class="brand"><span class="brand-dot"></span><span class="brand-name">Brindle</span></div>
  <nav class="main-nav">
    <a style="left:398px">Home</a>
    <a style="left:466px">About Brindle</a>
    <a style="left:573px">Download</a>
    <a style="left:665px">Contact</a>
  </nav>
</header>

<section class="hero" role="img" aria-label="Light grey photo of sheet music and headphones behind the app on a phone">
  <div class="hero-device" role="img" aria-label="Smartphone showing the Brindle app start screen"><div class="screen"></div></div>
  <div class="download-title heading">DOWNLOAD BRINDLE</div>
  <div class="download-panel">
    <div class="tagline heading">own the music</div>
    <p>Lorem Ipsum is simply dummy text of the printing and typesetting industry. Lorem Ipsum has been the industry's standard dummy text ever since</p>
    <div class="btn-more">READ MORE &gt;&gt;</div>
  </div>
  <div class="slider-dots"><span class="is-active"></span><span></span><span></span><span></span></div>
</section>

<section class="tweet">
  <div class="tweet-mark"></div>
  <div class="tweet-text heading">RT <span class="link">@brindleblog</span>: How I Stopped My Musicx ment<br>Spam <span class="link">http://brn.dl/pHJnZGJtG7</span></div>
  <div class="tweet-meta">about 4 days ago | @mk_hollis</div>
</section>

<section class="content-band">
  <h2 class="section-title heading" style="left:66px;top:12px">Latest News</h2>
  <article class="news-card" style="top:44px">
    <div class="thumb" role="img" aria-label="Photo of an old city building" style="background:linear-gradient(160deg,#9a9a98,#4e4d4b)"></div>
    <p>Lorem Ipsum is simply dummy text of the printing and typesetting industry. Lorem Ipsum has been the industry's text.</p>
    <span class="more">Readmore</span><span class="date">16 Jan 2014</span>
  </article>
  <article class="news-card" style="top:130px">
    <div class="thumb" role="img" aria-label="Photo of a singer on stage" style="background:linear-gradient(160deg,#8a8a88,#2f2f2f)"></div>
    <p>Lorem Ipsum is simply dummy text of the printing and typesetting industry. Lorem Ipsum has been the industry's text.</p>
    <span class="more">Readmore</span><span class="date">16 Jan 2014</span>
  </article>
  <article class="news-card" style="top:215px">
    <div class="thumb" role="img" aria-label="Photo of a crowd under purple concert lights" style="background:linear-gradient(160deg,#c9c3dc,#6d6387)"></div>
    <p>Lorem Ipsum is simply dummy text of the printing and typesetting industry. Lorem Ipsum has been the industry's text.</p>
    <span class="more">Readmore</span><span class="date">16 Jan 2014</span>
  </article>

  <h2 class="section-title heading" style="left:360px;top:14px">Welcome to Brindle</h2>
  <div class="welcome-box">
    <div class="welcome-photo" role="img" aria-label="Photo of hands playing an acoustic guitar"></div>
    <span class="drop-cap">L</span>orem Ipsum is simply dummy text of the printing and typesetting industry. Lorem Ipsum has been the industry's standard dummy text ever since the 1500s, when an unknown printer took a galley of type and scrambled it to make a type specimen book. It has survived not only five centuries, but also the leap into electronic typesetting, ive centuries, but also the leap into electronic typeset. Lorem Ipsum is simply dummy text of the printing and typesetting industry. Lorem Ipsum has been the industry's standard dummy text ever since the 1500s, when an unknown printer took a galley of type and scrambled it to make a type specimen book. It has survived not only five centuries, but also the leap into electronic typesetting, remaining essentially unchanged. It was popularised in the 1960s with the release of
  </div>
</section>

<section class="clients">
  <h2 class="section-title heading">Our Clients</h2>
  <div class="client-row" style="top:68px">
    <span>northwood</span><span>reedhall</span><span>tidepost</span><span>lowcart</span><span>emtone</span><span>circlebook</span><span>orbitplus</span><span>iNod</span><span><i></i>tunedesk</span>
  </div>
  <div class="client-row" style="top:90px">
    <span>farlist</span><span>mixdune</span><span>ourroom</span><span>clearvol</span><span>pelican</span><span>Echoland</span><span>wavefield</span><span>brightspin</span>
  </div>
  <div class="client-row" style="top:114px">
    <span>chirrup</span><span>indiehall</span><span>reelbox</span><span>viewtube</span><span><i></i>zephyr</span>
  </div>
</section>

<footer class="site-footer">
  <div class="footer-brand"><span class="brand-dot"></span><span class="brand-name">Brindle</span></div>
  <div class="copyright">Copyrights received @ 2014</div>
  <div class="social-links">
    <span style="background:#6ea25a"></span><span style="background:#3b5998"></span><span style="background:#2aa9e0"></span><span style="background:#0e76a8"></span><span style="background:#cb2027"></span><span style="background:#e6e6e6"></span>
  </div>
  <nav class="footer-nav"><a>Shop</a><a>Tour Dates</a><a>About</a><a>Archiver</a><a>Contact</a></nav>
</footer>

</body>
</html>
```